Larkmoor Heritage Guild Harvest Lantern Days Event Flyer - Historic Event

I need a flyer about the Larkmoor Heritage Guild's Harvest Lantern Days event October 8th and 9th. The centerpiece of Harvest Lantern Days is Civil War reenactments. I want the flyer to include the schedule of events and be eye catching on area bulletin boards. Our website is www.larkmoorheritageguild.org for more information and pictures. The website for the Tilden Rangers reenactors is http://www.tildenrangers.com/.

Target Market(s)

Our target market is middle ages (35-70) families and couples. Most are history buffs, especially about the Civil War.

Industry/Entity Type

Non-Profit

Font styles to use
Serif
Decorative
Script

Requirements
Must have
• The flyer must include the majority of the schedule attached - especially the battle times, museums, and anything including food.The dance on Saturday night is also important. The bottom of the flyer MUST say "Paid in part by Osgood County Visitor Fund Board"
Nice to have
• Pictures

```html
<!DOCTYPE html>
<html lang="en">
<head>
<meta charset="utf-8">
<title>Larkmoor Heritage Guild – Harvest Lantern Days Flyer</title>
<link href="https://fonts.googleapis.com/css2?family=Almendra:wght@400;700&family=Crimson+Text:ital,wght@0,400;0,600;1,600&family=Open+Sans:wght@600;700&display=swap" rel="stylesheet">
<style>
  :root {
    --backdrop: #dcdcdc;
    --parchment: #d9c48f;
    --parchment-light: #e6d5a6;
    --parchment-edge: #8a6a35;
    --maroon: #6b1f2e;
    --maroon-dark: #4e1420;
    --ink: #5a1a27;
    --white: #ffffff;
  }
  * { box-sizing: border-box; margin: 0; padding: 0; }
  html, body { width: 1200px; height: 1200px; overflow: hidden; }
  body { background: var(--backdrop); position: relative; }

  .flyer {
    position: absolute; left: 197px; top: 30px;
    width: 806px; height: 1140px; overflow: hidden;
    background:
      radial-gradient(ellipse at 50% 45%, var(--parchment-light) 0%, var(--parchment) 55%, #b89a5c 85%, var(--parchment-edge) 100%);
    box-shadow: 0 6px 18px rgba(0,0,0,.25);
  }

  .rule { position: absolute; left: 50px; right: 50px; height: 2px; background: var(--maroon); }
  .rule--top { top: 44px; }
  .rule--bottom { top: 212px; }

  .title {
    position: absolute; left: 0; right: 0; top: 58px;
    text-align: center; font-family: "Almendra", serif; font-weight: 700;
    color: var(--maroon); line-height: 1.1;
    text-shadow: 1px 1px 0 var(--parchment-light), -1px -1px 0 var(--parchment-light);
  }
  .title__guild { display: block; font-size: 50px; }
  .title__event { display: block; font-size: 52px; }

  .event-dates {
    position: absolute; right: 40px; top: 222px;
    font-family: "Open Sans", sans-serif; font-weight: 700;
    color: var(--maroon); font-size: 24px; line-height: 1.15; text-align: left;
    text-shadow: 1px 1px 0 var(--parchment-light);
  }
  .event-dates sup { font-size: 13px; }

  .photo {
    position: absolute; border: 6px solid var(--maroon);
    padding: 14px; background: #efe9dc;
  }
  .photo__fill { width: 100%; height: 100%; border-radius: 28px; }
  .photo--cabin { left: 40px; top: 320px; width: 330px; height: 285px; }
  .photo--cabin .photo__fill { background: linear-gradient(160deg, #7da04a 0%, #9a8a6a 45%, #6f5638 75%, #8c9a5a 100%); }
  .photo--workshop { left: 400px; top: 292px; width: 340px; height: 288px; }
  .photo--workshop .photo__fill { background: linear-gradient(170deg, #c9a46a 0%, #8a5a32 40%, #3b2a20 80%, #5a4a40 100%); }

  .section-title {
    position: absolute; left: 110px; top: 622px;
    font-family: "Almendra", serif; font-weight: 700; font-size: 50px;
    color: var(--maroon); white-space: nowrap;
    text-shadow: 1px 1px 0 var(--parchment-light);
  }

  .day { position: absolute; color: var(--ink); font-family: "Crimson Text", serif; }
  .day--saturday { left: 45px; top: 700px; width: 410px; }
  .day--sunday { left: 485px; top: 625px; width: 290px; }
  .day__heading {
    font-family: "Open Sans", sans-serif; font-weight: 600; font-size: 21px;
    color: var(--maroon); border-bottom: 1.5px solid var(--maroon);
    padding-bottom: 3px; margin-bottom: 8px; white-space: nowrap;
  }
  .day__note { font-style: italic; font-weight: 600; font-size: 20px; line-height: 1.15; margin-bottom: 8px; }
  .day__list { list-style: none; font-size: 15.5px; line-height: 1.3; }
  .day__list li { padding-left: 16px; position: relative; margin-bottom: 6px; }
  .day__list li::before {
    content: ""; position: absolute; left: 2px; top: 8px;
    width: 6px; height: 6px; border-radius: 50%; background: var(--maroon);
  }

  .sponsor-band {
    position: absolute; right: -40px; bottom: 120px;
    width: 420px; padding: 12px 26px;
    background: var(--maroon-dark); border-radius: 40px;
    transform: rotate(-32deg);
    font-family: "Open Sans", sans-serif; font-weight: 700;
    font-size: 22px; line-height: 1.2; color: var(--white); text-align: center;
  }
</style>
</head>
<body>
  <main class="flyer">
    <div class="rule rule--top"></div>
    <h1 class="title">
      <span class="title__guild">Larkmoor Heritage Guild’s</span>
      <span class="title__event">Harvest Lantern Days event</span>
    </h1>
    <div class="rule rule--bottom"></div>

    <p class="event-dates">8<sup>th</sup> &amp; 9<sup>th</sup><br>October</p>

    <figure class="photo photo--cabin">
      <div class="photo__fill" role="img" aria-label="Photo of a historic log cabin among trees"></div>
    </figure>
    <figure class="photo photo--workshop">
      <div class="photo__fill" role="img" aria-label="Photo of a canvas-roofed period workshop with a spinning wheel demonstration"></div>
    </figure>

    <h2 class="section-title">Events &amp; Time</h2>

    <section class="day day--saturday">
      <h3 class="day__heading">Saturday, October 8th, 2016</h3>
      <p class="day__note">Through the Day – Demonstrations and Speakers in various locations</p>
      <ul class="day__list">
        <li>10:00 AM – Battle by Tilden Rangers<br>Sponsored in part by Hollis Corner Markets</li>
        <li>11:30-1:00 – Chicken Biscuit Bake at Town Hall – Free Will Donation<br>Afternoon – Trolley and Buggy Rides</li>
        <li>1:00-4:00 Museums Opens</li>
        <li>1:30-2:00 Birthday Cake on Whitlow House Front Porch<br>Cake donated by Greenbough Grocers – Ashford City</li>
        <li>2:00 Battle by Tilden Rangers</li>
        <li>3:00-Sightseeing Cruise on the Spirit of Larkmoor</li>
        <li>6:00-? Dance at Town Hall with Turntable Band<br>Sponsored by Dr. Pellham</li>
      </ul>
    </section>

    <section class="day day--sunday">
      <h3 class="day__heading">Sunday, October 9th, 2016</h3>
      <ul class="day__list">
        <li>12:30 PM Parade on Main Street</li>
        <li>Afternoon – Buggy &amp; Trolley Rides</li>
        <li>1:00-4:00 Museums Open</li>
        <li>1:30 Battle by Tilden Rangers</li>
        <li>2:00- Pie Reception at Larkmoor Depot and Railroad History Museum</li>
        <li>3:00-Sightseeing Cruise</li>
      </ul>
    </section>

    <p class="sponsor-band">Paid in part by Osgood County Visitor Fund Board</p>
  </main>
</body>
</html>
```